New Managed IT company needs a business card

We are an IT management and support company that needs a business card design. I have a logo that I'll provide. Blues and blacks match the logo, but i'm open to anything. I want the card to help people take us seriously, but still have some energy and fun in it. The card should communicate stability and a solid company.

Target Market(s)

Target market includes Owners and Presidents at small businesses of 20 - 100 employees in the Pittsburgh PA area.

Industry/Entity Type

Information Technology

Contact Information for Business Card

i am open to other designs, but i imagine having only the logo on one side and then the logo plus all contact details on the other side.

Requirements
Must have
• Our logo
• Company name is optional if the logo makes it obvious
• A name - Lew Tasker
• A title - President
• A phone number - 724-XXX-XXXX
• A mobile phone number - 724-516-0471
• An email address - ltasker@brightlanetech.com
• a website - brightlanetech.com or www.brightlanetech.com
Nice to have
• some people tell me the logo feels like a superhero theme, some fun with that idea might be good. I'm open to ideas.
Should not have
• stock photos of people or computers - especially old looking stuff.

```html
<!DOCTYPE html>
<html lang="en">
<head>
<meta charset="utf-8">
<title>Bright Lane Tech — Business Card</title>
<link href="https://fonts.googleapis.com/css2?family=Tinos:wght@400;700&display=swap" rel="stylesheet">
<style>
  :root {
    --bg: #e9e6e1;
    --card-white: #ffffff;
    --card-black: #1b1b1d;
    --ink: #1e1e20;
    --accent: #1f96d8;
    --light: #f4f4f4;
  }
  * { box-sizing: border-box; margin: 0; padding: 0; }
  html, body { width: 1200px; height: 913px; overflow: hidden; }
  body {
    background: var(--bg);
    font-family: "Tinos", "Times New Roman", serif;
    position: relative;
  }
  .card {
    position: absolute;
    width: 560px;
    height: 320px;
    background: var(--card-white);
    box-shadow: 0 10px 28px rgba(0,0,0,.18);
    overflow: hidden;
  }
  .card--front { left: 70px; top: 90px; }
  .card--back { left: 570px; top: 500px; }

  .brand {
    position: absolute;
    display: flex;
    align-items: center;
    gap: 14px;
    color: var(--ink);
    font-weight: 700;
    text-transform: uppercase;
    letter-spacing: .08em;
    white-space: nowrap;
  }
  .brand__dot {
    border-radius: 50%;
    background: var(--accent);
    flex: none;
  }
  .card--front .brand { left: 50%; top: 50%; transform: translate(-50%, -50%); font-size: 34px; }
  .card--front .brand__dot { width: 54px; height: 54px; }
  .card--back .brand { left: 24px; top: 178px; font-size: 13px; gap: 8px; letter-spacing: .04em; }
  .card--back .brand__dot { width: 24px; height: 24px; }

  .back-art { position: absolute; inset: 0; }

  .contact {
    position: absolute;
    left: 318px;
    top: 62px;
    color: var(--light);
  }
  .contact__name {
    color: var(--accent);
    font-size: 29px;
    font-weight: 400;
    text-transform: uppercase;
    letter-spacing: .01em;
    line-height: 1;
  }
  .contact__title { font-size: 16px; margin-top: 3px; }
  .contact__list { list-style: none; margin-top: 22px; }
  .contact__item {
    display: flex;
    align-items: center;
    gap: 9px;
    font-size: 14.5px;
    line-height: 1;
    margin-bottom: 9px;
  }
  .contact__icon { width: 15px; height: 15px; flex: none; }
</style>
</head>
<body>

  <section class="card card--front" aria-label="Card front">
    <div class="brand"><span class="brand__dot"></span>Bright Lane Tech</div>
  </section>

  <section class="card card--back" aria-label="Card back">
    <svg class="back-art" viewBox="0 0 560 320" aria-hidden="true">
      <path d="M185 0 C 255 60 292 170 300 320 L560 320 L560 0 Z" fill="var(--card-black)"/>
      <path d="M118 0 C 185 28 238 110 258 250 C 230 140 190 60 150 20 C 140 10 128 4 118 0 Z" fill="var(--card-black)"/>
    </svg>

    <div class="brand"><span class="brand__dot"></span>Bright Lane Tech</div>

    <div class="contact">
      <h1 class="contact__name">Lew Tasker</h1>
      <p class="contact__title">President</p>
      <ul class="contact__list">
        <li class="contact__item">
          <svg class="contact__icon" viewBox="0 0 16 16"><circle cx="8" cy="8" r="8" fill="var(--accent)"/><path d="M5 4.5c.6-.5 1.2-.3 1.5.3l.5 1c.2.4 0 .8-.3 1l-.4.3c.4.9 1.1 1.6 2 2l.3-.4c.2-.3.6-.5 1-.3l1 .5c.6.3.8.9.3 1.5-.7.8-2 .9-3.4-.1-1.4-1-2.4-2.3-2.9-3.6-.3-1-.2-1.8.4-2.2z" fill="var(--card-black)"/></svg>
          724-XXX-XXXX
        </li>
        <li class="contact__item">
          <svg class="contact__icon" viewBox="0 0 16 16"><circle cx="8" cy="8" r="8" fill="var(--accent)"/><rect x="5.5" y="3.5" width="5" height="9" rx="1" fill="none" stroke="var(--card-black)" stroke-width="1.3"/><circle cx="8" cy="10.8" r=".6" fill="var(--card-black)"/></svg>
          724-516-0471
        </li>
        <li class="contact__item">
          <svg class="contact__icon" viewBox="0 0 16 16"><circle cx="8" cy="8" r="8" fill="var(--accent)"/><rect x="4" y="5.2" width="8" height="5.6" fill="var(--card-black)"/><path d="M4 5.4 8 8.4 12 5.4" fill="none" stroke="var(--accent)" stroke-width=".9"/></svg>
          ltasker@brightlanetech.com
        </li>
        <li class="contact__item">
          <svg class="contact__icon" viewBox="0 0 16 16"><circle cx="8" cy="8" r="8" fill="var(--accent)"/><circle cx="8" cy="8" r="4.5" fill="none" stroke="var(--card-black)" stroke-width="1.1"/><ellipse cx="8" cy="8" rx="2" ry="4.5" fill="none" stroke="var(--card-black)" stroke-width="1"/><path d="M3.5 8h9" stroke="var(--card-black)" stroke-width="1"/></svg>
          www.brightlanetech.com
        </li>
      </ul>
    </div>
  </section>

</body>
</html>
```